Vista Chapel - Giving Hope
Sleek, Simple, Modern - Identity Package
Project: Vista Chapel - Giving Hope
Vista Chapel - Giving Hope - Religion and Spirituality
Creative Brief
Use specific fonts
open to new fonts and font changes
Simple
Ben Holloway
Chief Innovation Officer
4182 Cedar Vale Rd Atlanta, Ga 30319
404-561-3297 x 318
benh@cedarvalefold.org
www.CedarValeFold.org
Need a new fresh look for our letterhead, envelopes, labels, B. Cards etc. Also need the letterhead in Monarch size w/ matching envelopes. No deisgns that look like a law firm or accounting firm. Sleek and Modern is important.
Leave area on Back of card to make notes / write. The web address and/or some of the address info can go on the back. use our tag line someplace on the card: "Giving Hope in Christ"

```html
<!DOCTYPE html>
<html lang="en">
<head>
<meta charset="utf-8">
<title>Vista Chapel – Identity Package</title>
<link href="https://fonts.googleapis.com/css2?family=Open+Sans:wght@400;700&display=swap" rel="stylesheet">
<style>
:root{
  --backdrop:#1d1f22;
  --paper:#ffffff;
  --ink:#222a30;
  --teal:#1f6f7d;
  --grey:#7a8288;
  --wave-deep:#1d6fb5;
  --wave-mid:#3fa3df;
  --wave-light:#a9dcf5;
}
*{margin:0;padding:0;box-sizing:border-box}
html,body{width:1200px;height:756px;overflow:hidden;background:var(--backdrop);font-family:"Open Sans",Arial,sans-serif;color:var(--ink)}
.board{position:relative;width:1200px;height:756px}
.sheet{position:absolute;background:var(--paper);overflow:hidden;box-shadow:0 2px 8px rgba(0,0,0,.5)}
.wave-band{position:absolute;left:0;width:100%;
  background:linear-gradient(180deg,var(--paper) 0%,var(--wave-light) 25%,var(--wave-mid) 50%,var(--wave-deep) 68%,var(--wave-light) 85%,var(--paper) 100%)}
.brand{position:absolute;display:flex;align-items:center;gap:5px}
.brand-dot{border-radius:50%;background:var(--ink);flex:none}
.brand-name{color:var(--teal);font-weight:700;white-space:nowrap}
.small{font-size:5px;line-height:1.5;color:var(--grey);position:absolute;white-space:nowrap}

.letterhead{left:84px;top:89px;width:461px;height:600px}
.letterhead .brand{left:22px;top:28px}
.letterhead .brand-dot{width:34px;height:34px}
.letterhead .brand-name{font-size:17px}
.letterhead .head-address{left:295px;top:30px}
.letterhead .head-contact{left:385px;top:30px}
.letterhead .wave-band{bottom:24px;height:90px}
.letterhead .web{right:22px;bottom:10px;font-weight:700;color:var(--ink)}

.card{width:192px;height:103px;border-radius:8px}
.card-front{left:566px;top:96px}
.card-front .brand{left:52px;top:28px}
.card-front .brand-dot{width:20px;height:20px}
.card-front .brand-name{font-size:10px}
.card-front .tagline{left:74px;top:56px;font-size:4.5px}
.card-front .wave-band{bottom:2px;height:32px}
.card-back{left:775px;top:96px}
.card-back .person{position:absolute;right:14px;top:10px;text-align:center}
.card-back .name{font-size:6px;font-weight:700;color:var(--teal)}
.card-back .role{font-size:4.5px;color:var(--grey)}
.card-back .details{right:16px;top:32px}
.card-back .wave-band{bottom:2px;height:36px}

.envelope{left:564px;top:223px;width:528px;height:221px}
.envelope .flap{position:absolute;inset:0;width:100%;height:100%}
.envelope .brand{left:50%;top:26px;transform:translateX(-50%)}
.envelope .brand-dot{width:24px;height:24px}
.envelope .web{left:50%;top:54px;transform:translateX(-50%);font-weight:700;color:var(--ink)}

.label{left:564px;top:461px;width:528px;height:228px}
.label .brand{left:14px;top:36px}
.label .brand-dot{width:30px;height:30px}
.label .brand-name{font-size:14px}
.label .wave-band{bottom:30px;height:70px}
.label .return{left:16px;bottom:10px;color:var(--ink)}
</style>
</head>
<body>
<main class="board">

  <section class="sheet letterhead">
    <div class="brand"><span class="brand-dot"></span><span class="brand-name">Vista Chapel</span></div>
    <p class="small head-address">4182 Cedar Vale Rd<br>Atlanta, Ga 30319</p>
    <p class="small head-contact">404-561-3297 x 318<br>404-561-3298 fax</p>
    <div class="wave-band" role="img" aria-label="Flowing blue wave band"></div>
    <p class="small web">www.CedarValeFold.org</p>
  </section>

  <section class="sheet card card-front">
    <div class="brand"><span class="brand-dot"></span><span class="brand-name">Vista Chapel</span></div>
    <p class="small tagline">Giving Hope in Christ</p>
    <div class="wave-band" role="img" aria-label="Flowing blue wave band"></div>
  </section>

  <section class="sheet card card-back">
    <div class="person"><p class="name">Ben Holloway</p><p class="role">Chief Innovation Officer</p></div>
    <p class="small details">4182 Cedar Vale Rd<br>Atlanta, Ga 30319<br>404-561-3297 x 318<br>benh@cedarvalefold.org</p>
    <div class="wave-band" role="img" aria-label="Flowing blue wave band"></div>
  </section>

  <section class="sheet envelope">
    <svg class="flap" viewBox="0 0 528 221" preserveAspectRatio="none" aria-hidden="true">
      <path d="M0 0 L264 90 L528 0" stroke="#d9dde0" stroke-width="1" fill="none"/>
    </svg>
    <div class="brand"><span class="brand-dot"></span></div>
    <p class="small web">www.CedarValeFold.org</p>
  </section>

  <section class="sheet label">
    <div class="brand"><span class="brand-dot"></span><span class="brand-name">Vista Chapel</span></div>
    <div class="wave-band" role="img" aria-label="Flowing blue wave band"></div>
    <p class="small return">4182 Cedar Vale Rd Atlanta, Ga 30319<br>404-561-3297 x 318</p>
  </section>

</main>
</body>
</html>
```